Flyer Design Project

Design for flyer, poster and web graphic for funday. Details attached. Event is a Funday with fair ground rides, bumper cars, stalls, food, BBQ

Target Market(s)

Muslim Families with young children

Industry/Entity Type

Event

Requirements
Should not have
• No pictures of living beings or creatures. Silhouettes acceptable.

```html
<!DOCTYPE html>
<html lang="en">
<head>
<meta charset="utf-8">
<title>Family Fun Day 10 – Brightpath Foundation</title>
<link rel="stylesheet" href="https://fonts.googleapis.com/css2?family=Luckiest+Guy&family=Open+Sans:wght@400;700;800&display=swap">
<style>
:root{
  --sky-deep:#0a1f6e;
  --sky-mid:#1746c4;
  --sky-glow:#3d8bf0;
  --lime:#b8e62a;
  --lime-light:#e4f86a;
  --grass:#5cae1e;
  --grass-dark:#2f7d12;
  --grass-pale:#c9ec7d;
  --ink-blue:#0b2a8a;
  --white:#ffffff;
}
*{margin:0;padding:0;box-sizing:border-box}
html,body{width:849px;height:1200px;overflow:hidden;background:var(--sky-deep)}
.flyer{
  position:relative;width:849px;height:1200px;overflow:hidden;
  font-family:"Open Sans",Arial,sans-serif;color:var(--white);
  background:radial-gradient(ellipse at 50% 30%,var(--sky-glow) 0%,var(--sky-mid) 35%,var(--sky-deep) 85%);
}
.butterfly{position:absolute;left:0;top:0;width:140px;height:165px;border-radius:40% 55% 45% 50%;
  background:linear-gradient(135deg,#f39a1e,#c2570b)}
.brand{position:absolute;left:300px;top:18px;display:flex;align-items:center;gap:12px}
.brand-dot{width:20px;height:20px;border-radius:50%;background:var(--lime)}
.brand-name{font-weight:800;font-size:40px;line-height:1;color:var(--white);text-align:center}
.brand-name small{display:block;font-size:16px;font-weight:700;letter-spacing:5px;margin-top:4px}
.title{position:absolute;left:150px;top:100px;width:560px;font-family:"Luckiest Guy",Impact,sans-serif;
  font-weight:400;color:var(--lime);line-height:.95;text-align:center;transform:rotate(-3deg);white-space:nowrap}
.title .t1{display:block;font-size:100px}
.title .t2{display:block;font-size:112px}
.title .num{position:absolute;right:-110px;top:30px;font-size:96px;color:var(--lime-light)}
.jumper{position:absolute;right:15px;top:200px;width:130px;height:170px;border-radius:30%;
  background:linear-gradient(180deg,rgba(0,0,20,.0),rgba(0,0,20,.55))}
.event-date{position:absolute;left:0;right:0;top:335px;text-align:center;line-height:1.3}
.event-date h2{font-weight:800;font-size:36px}
.event-date h2 sup{font-size:20px}
.event-date .time{font-weight:700;font-size:22px}
.event-date .venue{font-weight:700;font-size:19px}
.summary{position:absolute;left:150px;top:478px;width:480px;text-align:center;font-weight:700;font-size:19px;line-height:1.32}
.children{position:absolute;left:610px;top:590px;width:230px;height:150px;background:linear-gradient(180deg,rgba(10,40,10,.1),rgba(10,40,10,.55));border-radius:40% 40% 10% 10%}
.hill{position:absolute;left:-80px;right:-80px;top:620px;height:620px;border-radius:60% 60% 0 0/25% 25% 0 0;
  background:linear-gradient(180deg,var(--grass) 0%,var(--grass-pale) 35%,var(--white) 75%)}
.photo{position:absolute;border:5px solid var(--white);border-radius:50%}
.photo.castle{left:0;top:610px;width:170px;height:195px;border-radius:16px;border:none;background:linear-gradient(160deg,#e5322b,#f2c21a 60%,#2a7be0)}
.photo.rides{left:170px;top:595px;width:160px;height:155px;background:linear-gradient(135deg,#7fbcef,#d94a3a)}
.photo.cars{left:370px;top:720px;width:270px;height:135px;background:linear-gradient(135deg,#2d2d6e,#f07a1d)}
.photo.carousel{left:650px;top:765px;width:185px;height:140px;background:linear-gradient(135deg,#c7893a,#f5d68a)}
.dress{position:absolute;left:40px;top:865px;font-style:italic;font-weight:700;font-size:15px;line-height:1.3;color:var(--ink-blue);text-align:center}
.contact{position:absolute;left:200px;top:900px;font-size:18px;line-height:1.4;color:var(--ink-blue)}
.contact b{font-weight:700}
.entry{position:absolute;right:60px;top:995px;text-align:right;font-weight:700;font-size:18px;line-height:1.4;color:var(--ink-blue)}
.footer{position:absolute;left:0;right:0;bottom:0;height:80px;background:var(--grass-dark);
  display:flex;align-items:center;justify-content:center;font-weight:800;font-size:16.5px;white-space:nowrap}
</style>
</head>
<body>
<main class="flyer">
  <div class="butterfly" role="img" aria-label="Orange butterfly illustration"></div>
  <div class="brand"><span class="brand-dot"></span><span class="brand-name">brightpath<small>foundation</small></span></div>
  <h1 class="title"><span class="t1">Family</span><span class="t2">Fun Day</span><span class="num">10</span></h1>
  <div class="jumper" role="img" aria-label="Silhouette of a bungee jumper on a rope"></div>

  <section class="event-date">
    <h2>Sunday 9<sup>th</sup> June</h2>
    <p class="time">11am – 7pm</p>
    <p class="venue">Ashdown Field (off Ashdown Road),<br>Larkfield Park, Ilford, Essex, IG9 2ZX</p>
  </section>

  <p class="summary">A fun pack day for all the family,<br>Lots of stalls, including barbecue and food stalls<br>Sisters-only area, kids zone with bouncy castle,<br>funfair rides, games arts &amp; crafts</p>

  <div class="hill"></div>
  <div class="children" role="img" aria-label="Silhouettes of children jumping and playing"></div>
  <div class="photo castle" role="img" aria-label="Inflatable bouncy castle"></div>
  <div class="photo rides" role="img" aria-label="Funfair ride"></div>
  <div class="photo cars" role="img" aria-label="Bumper cars"></div>
  <div class="photo carousel" role="img" aria-label="Carousel ride"></div>

  <p class="dress">MODEST<br>DRESS<br>REQUIRED</p>
  <div class="contact">
    <p>For further information please email:<br><b>funday@brightpathschool.co.uk</b></p>
    <p>For stalls booking please email:<br><b>funday@brightpathschool.co.uk</b></p>
    <p><b>www.brightpath-trust.co.uk</b></p>
  </div>
  <p class="entry">Entrance £2 for ALL<br>FREE for under 3<br>Parking on site £3 per vehicle</p>

  <footer class="footer">All proceeds from this Funday go towards the growth of Brightpath Foundation</footer>
</main>
</body>
</html>
```